CloudRiver Business Card

I need something that flows with the logo and looks professional but creative. I included the thumbnail file of the photo but will upload the source file once I have it. Colors of business card should flow. I am interested in doing the translucent clear plastic cards as well. My company is called CloudRiver in one word and the contact details are below:

Dale Hollings
555-318-4720
www.CloudRiverTx.example
dhollings_47@mailbox.example
Updates

Too much red. I'd rather focus on the blue and put some silver or grey in there.

New Files uploaded. Like the designs so far and am looking forward to seeing more.

Looking for a whole new direction. Let's forget about the plastic card. Let's focus on the blue more than red. I still haven't seen something that really grabs me.

Industry/Entity Type

Plastic

```html
<!DOCTYPE html>
<html lang="en">
<head>
<meta charset="utf-8">
<title>CloudRiver Business Card</title>
<link rel="stylesheet" href="https://fonts.googleapis.com/css2?family=Lato:wght@400;700&display=swap">
<style>
  :root {
    --page: #e9e7e3;
    --card: #1d1d1f;
    --card-edge: #2a2a2d;
    --blue: #1f7fc0;
    --blue-band: #3a7fb5;
    --red: #d8343c;
    --silver: #c9c9cb;
    --name-grey: #cfcfd1;
  }
  * { box-sizing: border-box; margin: 0; padding: 0; }
  html, body {
    width: 1200px; height: 1000px; overflow: hidden;
    background: var(--page);
    font-family: "Lato", sans-serif;
  }
  .canvas {
    width: 1200px; height: 1000px;
    display: flex; flex-direction: column; align-items: center; justify-content: center;
    gap: 40px;
  }
  .card {
    position: relative;
    width: 760px; height: 434px;
    border-radius: 14px;
    background: linear-gradient(160deg, var(--card-edge) 0%, var(--card) 55%, #18181a 100%);
    box-shadow: 0 8px 24px rgba(0,0,0,0.25);
    overflow: hidden;
  }
  .card-front { display: flex; align-items: center; justify-content: center; }
  .wordmark {
    font-weight: 700;
    color: var(--blue);
    letter-spacing: -0.5px;
    line-height: 1;
  }
  .card-front .wordmark { font-size: 104px; }
  .card-back .wordmark {
    position: absolute; left: 44px; top: 42px;
    font-size: 58px;
  }
  .holder-name {
    position: absolute; right: 70px; top: 56px;
    font-size: 30px; font-weight: 700; letter-spacing: 1px;
    color: var(--name-grey);
  }
  .contact-list {
    position: absolute; right: 48px; top: 222px;
    list-style: none;
    display: flex; flex-direction: column; align-items: flex-end; gap: 10px;
  }
  .contact-item {
    display: flex; align-items: center; gap: 14px;
    font-size: 22px; color: var(--blue);
  }
  .contact-icon { width: 20px; height: 20px; flex: none; }
  .stripe-bar {
    position: absolute; left: 0; bottom: 0;
    width: 760px; height: 26px;
  }
</style>
</head>
<body>
<main class="canvas">
  <section class="card card-front" aria-label="Card front">
    <h1 class="wordmark">CloudRiver</h1>
  </section>

  <section class="card card-back" aria-label="Card back">
    <p class="wordmark">CloudRiver</p>
    <p class="holder-name">Dale Hollings</p>
    <ul class="contact-list">
      <li class="contact-item">555-318-4720
        <svg class="contact-icon" viewBox="0 0 20 20" aria-hidden="true">
          <path d="M4 2 L7.5 2 L8.5 6 L6.5 7.5 C7.5 10 9.5 12 12 13 L13.5 11 L17.5 12 L17.5 15.5 C17.5 16.5 16.5 17.5 15.5 17.5 C8.5 17.5 2.5 11.5 2.5 4 C2.5 3 3 2 4 2 Z" fill="var(--red)"/>
          <path d="M12 2.5 A6 6 0 0 1 17.5 8" stroke="var(--red)" stroke-width="1.6" fill="none"/>
          <path d="M11.5 5.5 A3 3 0 0 1 14.5 8.5" stroke="var(--red)" stroke-width="1.6" fill="none"/>
        </svg>
      </li>
      <li class="contact-item">www.CloudRiverTx.example
        <svg class="contact-icon" viewBox="0 0 20 20" aria-hidden="true">
          <rect x="1.5" y="4" width="17" height="12" rx="1" fill="var(--red)"/>
          <path d="M2 4.5 L10 11 L18 4.5" stroke="var(--card)" stroke-width="1.5" fill="none"/>
        </svg>
      </li>
      <li class="contact-item">dhollings_47@mailbox.example
        <svg class="contact-icon" viewBox="0 0 20 20" aria-hidden="true">
          <circle cx="10" cy="10" r="8" fill="var(--red)"/>
          <ellipse cx="10" cy="10" rx="3.5" ry="8" stroke="var(--card)" stroke-width="1.2" fill="none"/>
          <line x1="2" y1="10" x2="18" y2="10" stroke="var(--card)" stroke-width="1.2"/>
        </svg>
      </li>
    </ul>
    <svg class="stripe-bar" viewBox="0 0 760 26" aria-hidden="true">
      <polygon points="0,4 190,4 196,26 0,26" fill="var(--blue-band)"/>
      <polygon points="205,4 400,4 394,26 211,26" fill="var(--red)"/>
      <polygon points="410,4 760,4 760,26 403,26" fill="var(--silver)"/>
    </svg>
  </section>
</main>
</body>
</html>
```